BRAVEN POWERLINE SERVICES needs a vibrant design for electrical contracting work.

I require a card design for my own electrical contracting business. I will be doing a lot of domestic and commercial work, including things such as repairs, maintenance, lighting, installations and various others. LED lighting and energy efficiency will be a big part of my business. I wish not to have childish pictures such as light bulbs in the design, but rather a smart and modern looking card which incorporates my logo colours and perhaps the same lighting strike within the faded background of the card.

Target Market(s)

Residential and Commercial property owners.

Industry/Entity Type

Electrical

Contact Information for Business Card

Dalen Voskic
EC40923
Phone Number: 0417 358 942
Email: dalen@bravenpowerline.com

Font styles to use
Serif
Sans Serif

Requirements
Must have
• My Logo and associated colours.
Nice to have
• Some form of shapes splitting the card into different colours related to the colours of my logo. Electric Blue, Silver/Grey and White.
Should not have
• Childish pictures and symbols such as light bulbs.

```html
<!DOCTYPE html>
<html lang="en">
<head>
<meta charset="utf-8">
<title>Braven Powerline Services – Business Card</title>
<link rel="stylesheet" href="https://fonts.googleapis.com/css2?family=Jost:wght@400;600&display=swap">
<style>
  :root {
    --page-bg: #1a1a1a;
    --card-black: #0a0a0a;
    --card-black-soft: #1c1c1c;
    --card-white: #f4f4f4;
    --card-silver: #cfcfcf;
    --text-dark: #1e1e1e;
    --logo-light: #e8e8e8;
  }
  html, body {
    margin: 0;
    padding: 0;
    width: 1200px;
    height: 1001px;
    overflow: hidden;
    background: var(--page-bg);
    font-family: "Jost", "Futura", sans-serif;
  }
  .canvas {
    position: relative;
    width: 1200px;
    height: 1001px;
  }
  .business-card {
    position: absolute;
    left: 150px;
    top: 243px;
    width: 900px;
    height: 514px;
    border-radius: 36px;
    overflow: hidden;
    box-shadow: 0 20px 50px rgba(0,0,0,0.6);
  }
  .card-shapes {
    position: absolute;
    inset: 0;
    display: block;
  }
  .brand-lockup {
    position: absolute;
    left: 120px;
    top: 150px;
    display: flex;
    align-items: center;
    gap: 18px;
  }
  .brand-dot {
    width: 58px;
    height: 58px;
    border-radius: 50%;
    background: var(--logo-light);
    flex: none;
  }
  .brand-name {
    color: var(--logo-light);
    font-weight: 600;
    font-size: 34px;
    letter-spacing: 2px;
    line-height: 1.05;
    margin: 0;
  }
  .contact-block {
    position: absolute;
    left: 0;
    right: 0;
    top: 400px;
    text-align: center;
    color: var(--text-dark);
    font-size: 22px;
    font-weight: 400;
    line-height: 1.3;
    letter-spacing: 0.5px;
  }
  .contact-line { margin: 0; }
  .contact-gap { display: inline-block; width: 40px; }
</style>
</head>
<body>
<main class="canvas">
  <section class="business-card">
    <svg class="card-shapes" viewBox="0 0 900 514" preserveAspectRatio="none" aria-hidden="true">
      <defs>
        <linearGradient id="whiteArea" x1="0" y1="0" x2="0" y2="1">
          <stop offset="0" stop-color="#d9d9d9"/>
          <stop offset="0.35" stop-color="#f6f6f6"/>
          <stop offset="1" stop-color="#ececec"/>
        </linearGradient>
        <linearGradient id="blackArea" x1="0" y1="0" x2="1" y2="1">
          <stop offset="0" stop-color="#050505"/>
          <stop offset="0.6" stop-color="#111111"/>
          <stop offset="1" stop-color="#1e1e1e"/>
        </linearGradient>
      </defs>
      <rect width="900" height="514" fill="url(#whiteArea)"/>
      <path d="M0 0 H900 V175 C720 235 520 300 260 320 C150 328 60 328 0 322 Z" fill="var(--card-silver)"/>
      <path d="M0 0 H900 V160 C720 222 520 285 260 304 C150 312 60 312 0 306 Z" fill="url(#blackArea)"/>
    </svg>
    <div class="brand-lockup">
      <span class="brand-dot"></span>
      <p class="brand-name">BRAVEN POWERLINE<br>SERVICES</p>
    </div>
    <div class="contact-block">
      <p class="contact-line">Dalen Voskic EC40923<span class="contact-gap"></span>Phone Number: 0417 358 942</p>
      <p class="contact-line">Email: dalen@bravenpowerline.com</p>
    </div>
  </section>
</main>
</body>
</html>
```